Email Signature

Our company is having its 10th anniversary in 2021. We would like a new email signature to celebrate the occasion. Attached is our business card design.
Please refer to our website for actual contact details.
www.corvanhold.com.au

Industry/Entity Type

Real Estate

Requirements
Must have
• Our logo
Email
Contact Numbers
Address
Website address

Celebrating 10 years in 2021
Nice to have
• Something that blends the designs of our website and business card

```html
<!DOCTYPE html>
<html lang="en">
<head>
<meta charset="utf-8">
<title>Corvan Hold – Email Signature</title>
<link rel="stylesheet" href="https://fonts.googleapis.com/css2?family=Exo+2:wght@700&family=Mulish:wght@400&family=Arimo:wght@400&display=swap">
<style>
  :root {
    --brand-blue: #1f5fa8;
    --sky-blue: #3a9ad6;
    --accent-blue: #0a84c8;
    --ink: #1a1a1a;
    --paper: #ffffff;
  }
  html, body {
    margin: 0;
    padding: 0;
    width: 1200px;
    height: 469px;
    overflow: hidden;
    background: var(--paper);
  }
  .signature {
    position: relative;
    width: 1200px;
    height: 469px;
    background: var(--paper);
    font-family: "Mulish", sans-serif;
    color: var(--ink);
  }
  .brand {
    position: absolute;
    left: 53px;
    top: 180px;
    display: flex;
    align-items: center;
    gap: 12px;
  }
  .brand-square {
    width: 22px;
    height: 22px;
    background: var(--brand-blue);
  }
  .brand-name {
    font-family: "Exo 2", sans-serif;
    font-weight: 700;
    font-size: 38px;
    letter-spacing: 1px;
    color: var(--brand-blue);
    line-height: 1;
  }
  .skyline {
    position: absolute;
    left: 0;
    top: 232px;
    width: 1200px;
    height: 196px;
    background: linear-gradient(to bottom,
      rgba(58,154,214,0.85) 0%,
      rgba(90,175,225,0.55) 30%,
      rgba(170,215,240,0.25) 70%,
      rgba(255,255,255,0) 100%);
  }
  .contact-list {
    position: absolute;
    left: 53px;
    top: 309px;
    margin: 0;
    padding: 0;
    list-style: none;
    font-size: 11.5px;
    line-height: 13px;
  }
  .contact-item {
    display: flex;
    align-items: flex-start;
    height: 28.3px;
  }
  .contact-icon {
    width: 14px;
    height: 14px;
    margin-right: 14px;
    flex: none;
  }
  .anniversary {
    position: absolute;
    left: 0;
    top: 0;
    width: 1200px;
    height: 469px;
    font-family: "Arimo", sans-serif;
    color: var(--accent-blue);
  }
  .anniversary span {
    position: absolute;
    line-height: 1;
  }
  .anniversary .word-celebrating {
    left: 843px;
    top: 358px;
    font-size: 28px;
  }
  .anniversary .number {
    left: 978px;
    top: 302px;
    font-size: 122px;
    letter-spacing: -8px;
  }
  .anniversary .word-years {
    left: 1103px;
    top: 367px;
    font-size: 28px;
  }
</style>
</head>
<body>
  <div class="signature">
    <div class="skyline" role="img" aria-label="Light blue city skyline silhouette fading into white"></div>

    <div class="brand">
      <div class="brand-square"></div>
      <div class="brand-name">CORVAN HOLD</div>
    </div>

    <ul class="contact-list">
      <li class="contact-item">
        <svg class="contact-icon" viewBox="0 0 14 14"><rect x="4" y="1" width="7" height="12" rx="1" fill="none" stroke="#1a1a1a" stroke-width="1.3"/><line x1="6.5" y1="11" x2="8.5" y2="11" stroke="#1a1a1a"/></svg>
        <span>555-204-3388</span>
      </li>
      <li class="contact-item">
        <svg class="contact-icon" viewBox="0 0 14 14"><path d="M1 5 Q7 1 13 5 L11 7 L9 5.5 L5 5.5 L3 7 Z" fill="#1a1a1a"/><rect x="3" y="7" width="8" height="5" rx="1" fill="#1a1a1a"/></svg>
        <span>555-318-6240</span>
      </li>
      <li class="contact-item">
        <svg class="contact-icon" viewBox="0 0 14 14"><rect x="1" y="3" width="12" height="8" fill="#1a1a1a"/><path d="M1 3 L7 8 L13 3" fill="none" stroke="#fff" stroke-width="1"/></svg>
        <span>r.marlow@corvanhold.com</span>
      </li>
      <li class="contact-item">
        <svg class="contact-icon" viewBox="0 0 14 14"><circle cx="7" cy="7" r="5.5" fill="none" stroke="#1a1a1a" stroke-width="1.4"/><path d="M4 5 Q6 4 7 6 Q6 8 8 9 Q7 11 6 11" fill="none" stroke="#1a1a1a" stroke-width="1.2"/></svg>
        <span>www.corvanhold.com.au</span>
      </li>
      <li class="contact-item">
        <svg class="contact-icon" viewBox="0 0 14 14"><path d="M7 13 Q2 7 2 5 A5 5 0 0 1 12 5 Q12 7 7 13 Z" fill="#1a1a1a"/><circle cx="7" cy="5" r="1.8" fill="#fff"/></svg>
        <span>2740 Harbor Street #210<br>Westfield Bay, Florida 33901</span>
      </li>
    </ul>

    <div class="anniversary">
      <span class="word-celebrating">Celebrating</span>
      <span class="number">10</span>
      <span class="word-years">Years</span>
    </div>
  </div>
</body>
</html>
```